Stationary (Business Cards, envelopes, cover letters, etc) for HARBOR LANTERN PARTNERS
The Harbor Lantern Partners
Stationary (Business Cards, envelopes, cover letters, etc) for HARBOR LANTERN PARTNERS - Business Opportunities
Creative Brief
Professional
Rodrigo Velasco Brennan
Av. Ignacio Marroquín 718 B Col. Los Pinos Altos México DF CP 01482 México
rvelasco@hlp-example.mx
www.hlp-example.mx
First impressions have high impact, so in terms of the business card, it has to be something that's out of the box. The card is used to present ourselves to another party or prospect, but it also has to have a high impact message, either by an image or a phrase that comes attached in the back side. It could be some key points of a preview success case. So the back side has to have a marketing application. It has to be a card that will stand out, so much that it will be shown and passed around. In design and in materials (maybe???), although win the materials it will have a high impact on the costs of production. It has to be standard size, so it fits in every wallet thus avoiding on being thrown somewhere.
Concepts
Business Card and Stationary Project for a multifaceted corporation
Stationary for holding company
Business cards for RFTV - Investimentos e Administrações
mitiha mitiha
GREAT NEWS! WE'VE EXTENDED TO THIS FRIDAY! KEEP UP THE GREAT WORK!!!
Hi designers! GREAT JOB! We are want to decide today (our time) the winner. Please if you have any questions, let us know. Try to show as much applications as possible, i.e. we're now in a digital world so some digital applications we'll be considered for higher points. Have seen proposals in blue and gray (predominant colors and mixed), but none in orange. Let's see some! *Don't use curved lines in your design proposals. THANKS!
Hi, first of all I want to thank each and every one of you for accepting in working on our project. GREAT DESIGNS !!!!! Something we don't want is the lines that make a "curve" to separate content. I've seen a lot of those in the market and we want to be ORIGINAL. As I said in the brief, we want our cards to be saved as something awsome, and to be shown to other people. Material: sent your proposals of other materials, however if you can also send the specificatiosn of that material so we can see the cost of printing in them. Remember that it's not only the business cards but the stationary. KEEP UP THE GREAT JOB! CREATE DESIGN!

```html
<!DOCTYPE html>
<html lang="en">
<head>
<meta charset="utf-8">
<title>The Harbor Lantern Partners – Business Cards</title>
<link rel="stylesheet" href="https://fonts.googleapis.com/css2?family=Cinzel:wght@400;600&family=EB+Garamond:wght@400&display=swap">
<style>
  :root{
    --backdrop:#7e7f81;
    --card-black:#0b0b0c;
    --card-white:#ffffff;
    --accent-orange:#f28a1e;
    --accent-blue:#2a9fd8;
    --ink:#333333;
    --ink-light:#f2f2f2;
  }
  html,body{margin:0;padding:0;width:1200px;height:908px;overflow:hidden;background:var(--backdrop);}
  .stage{position:relative;width:1200px;height:908px;}
  .card{position:absolute;left:300px;width:600px;height:343px;border-radius:18px;overflow:hidden;box-shadow:0 10px 24px rgba(0,0,0,.35);}
  .card-front{top:92px;background:var(--card-black);}
  .card-back{top:484px;background:var(--card-white);}
  .card-shapes{position:absolute;inset:0;width:100%;height:100%;}

  .front-name{position:absolute;left:60px;top:132px;width:320px;text-align:center;color:var(--ink-light);
    font-family:"Cinzel",serif;font-weight:400;}
  .front-name .the{display:block;font-size:14px;letter-spacing:4px;}
  .front-name .main{display:block;font-size:23px;letter-spacing:2px;line-height:1.25;}
  .front-rule{position:absolute;height:1px;background:var(--ink-light);opacity:.8;}
  .front-mark{position:absolute;left:420px;top:96px;width:130px;height:130px;background:var(--accent-orange);}

  .back-brand{position:absolute;left:40px;top:40px;display:flex;align-items:center;gap:12px;}
  .back-brand .mark{width:30px;height:30px;background:var(--accent-blue);}
  .back-brand .name{font-family:"Cinzel",serif;font-weight:400;color:var(--ink);font-size:16px;letter-spacing:1px;line-height:1.2;}
  .address{position:absolute;left:40px;top:112px;width:250px;font-family:"EB Garamond",serif;font-size:14px;line-height:1.35;color:var(--ink);margin:0;}
  .contacts{position:absolute;left:40px;top:190px;list-style:none;margin:0;padding:0;font-family:"EB Garamond",serif;font-size:14px;color:var(--ink);}
  .contacts li{display:flex;align-items:center;gap:8px;line-height:22px;}
  .contacts svg{width:13px;height:13px;flex:none;}
  .person-name{position:absolute;right:28px;top:44px;font-family:"Cinzel",serif;font-size:15px;letter-spacing:.5px;color:var(--accent-blue);white-space:nowrap;}
</style>
</head>
<body>
<main class="stage">

  <section class="card card-front" aria-label="Business card front">
    <div class="front-rule" style="left:96px;top:140px;width:70px"></div>
    <div class="front-rule" style="left:274px;top:140px;width:70px"></div>
    <div class="front-name">
      <span class="the">The</span>
      <span class="main">Harbor Lantern Partners</span>
    </div>
    <div class="front-mark"></div>
  </section>

  <section class="card card-back" aria-label="Business card back">
    <svg class="card-shapes" viewBox="0 0 600 343" preserveAspectRatio="none">
      <polygon points="308,0 600,0 600,343 462,343" fill="var(--accent-orange)"/>
      <polygon points="318,0 600,0 600,343 472,343" fill="var(--card-black)"/>
    </svg>

    <div class="back-brand">
      <div class="mark"></div>
      <div class="name">The Harbor Lantern<br>Partners</div>
    </div>

    <p class="address">Av. Ignacio Marroquín 718 B<br>Col. Los Pinos Altos<br>México DF CP 01482, México</p>

    <ul class="contacts">
      <li><svg viewBox="0 0 13 13"><circle cx="6.5" cy="6.5" r="6.5" fill="var(--accent-orange)"/><path d="M4 3.5l1.5 1.5-1 1 2.5 2.5 1-1 1.5 1.5-1 1C6 10 3 7 3 4.5z" fill="#fff"/></svg>(55) 40 123 0000</li>
      <li><svg viewBox="0 0 13 13"><circle cx="6.5" cy="6.5" r="6.5" fill="var(--accent-orange)"/><rect x="4.5" y="3" width="4" height="7" rx="1" fill="#fff"/></svg>5255 1 0000 2468</li>
      <li><svg viewBox="0 0 13 13"><circle cx="6.5" cy="6.5" r="6.5" fill="var(--accent-orange)"/><rect x="3" y="4.2" width="7" height="4.6" fill="#fff"/></svg>rvelasco@hlp-example.mx</li>
      <li><svg viewBox="0 0 13 13"><circle cx="6.5" cy="6.5" r="6.5" fill="var(--accent-orange)"/><circle cx="6.5" cy="6.5" r="3.2" fill="none" stroke="#fff" stroke-width="1"/></svg>www.hlp-example.mx</li>
    </ul>

    <div class="person-name">Rodrigo Velasco Brennan</div>
  </section>

</main>
</body>
</html>
```